Business Card for plovrix

Create a Business Card with an existing logo for plovrix AG. We are a Information Technology company that does consulting and developing SW to automate business processes. The main colors are given from the logo.

Industry/Entity Type

Business

Requirements
Nice to have
• we use a a font style Century Gothic in our documents

```html
<!DOCTYPE html>
<html lang="en">
<head>
<meta charset="utf-8">
<title>plovrix AG – Business Card</title>
<link rel="stylesheet" href="https://fonts.googleapis.com/css2?family=Didact+Gothic&family=Cinzel:wght@400;500&display=swap">
<style>
  :root {
    --bg-light: #2aa204;
    --bg-dark: #166a00;
    --card-black: #000000;
    --card-white: #ffffff;
    --brand-green: #4fae2b;
    --brand-blue: #2a8fd8;
    --ink: #2b2b2b;
    --ink-soft: #5a5a5a;
  }
  * { margin: 0; padding: 0; box-sizing: border-box; }
  html, body { width: 1200px; height: 1200px; overflow: hidden; }
  body {
    position: relative;
    background: radial-gradient(circle at 45% 45%, var(--bg-light) 0%, var(--bg-dark) 75%);
    font-family: "Didact Gothic", "Century Gothic", sans-serif;
  }
  .card { position: absolute; overflow: hidden; }

  /* Front side */
  .card--front {
    left: 168px; top: 538px; width: 499px; height: 277px;
    background: var(--card-black);
  }
  .card--front .floor-glow {
    position: absolute; left: 180px; bottom: 0; width: 320px; height: 40px;
    background: radial-gradient(ellipse at 60% 100%, rgba(255,255,255,0.28), rgba(255,255,255,0) 70%);
  }
  .wordmark { position: absolute; display: flex; align-items: center; }
  .wordmark__dot { border-radius: 50%; background: var(--brand-blue); }
  .wordmark__name { line-height: 1; }
  .card--front .wordmark { left: 72px; top: 112px; gap: 14px; }
  .card--front .wordmark__dot { width: 52px; height: 52px; }
  .card--front .wordmark__name { font-size: 31px; color: var(--ink-soft); }

  /* Back side */
  .card--back {
    left: 679px; top: 318px; width: 278px; height: 498px;
    background: var(--card-white);
  }
  .card--back .wordmark { left: 44px; top: 90px; gap: 12px; }
  .card--back .wordmark__dot { width: 44px; height: 44px; }
  .card--back .wordmark__name { font-size: 36px; color: var(--ink); }

  .person { position: absolute; left: 41px; top: 296px; }
  .person__name {
    font-family: "Cinzel", serif; font-size: 11px; letter-spacing: 2px; color: var(--ink);
  }
  .person__role {
    font-family: "Cinzel", serif; font-size: 10px; letter-spacing: 1.5px; color: var(--brand-green); margin-top: 1px;
  }
  .address {
    position: absolute; left: 41px; top: 337px;
    font-size: 10.5px; letter-spacing: 1.3px; line-height: 14px; color: var(--ink);
  }
  .contacts { position: absolute; left: 39px; top: 378px; list-style: none; }
  .contacts li {
    display: flex; align-items: center; gap: 14px; height: 16.5px;
    font-size: 10.5px; letter-spacing: 1.3px; color: var(--ink);
  }
  .contacts svg { width: 12px; height: 12px; flex: none; }
  .card--back .band {
    position: absolute; left: 0; bottom: 0; width: 100%; height: 16px; background: var(--brand-green);
  }
</style>
</head>
<body>
  <section class="card card--front" aria-label="Business card front">
    <div class="floor-glow"></div>
    <div class="wordmark">
      <span class="wordmark__dot"></span>
      <span class="wordmark__name">plovrix</span>
    </div>
  </section>

  <section class="card card--back" aria-label="Business card back">
    <div class="wordmark">
      <span class="wordmark__dot"></span>
      <span class="wordmark__name">plovrix</span>
    </div>

    <div class="person">
      <p class="person__name">Lukas Brenner</p>
      <p class="person__role">CEO</p>
    </div>

    <p class="address">Talweg 12, 5400 Baden<br>Switzerland</p>

    <ul class="contacts">
      <li>
        <svg viewBox="0 0 12 12" aria-hidden="true"><path d="M1 4 Q6 0 11 4 L9.5 5.5 L8 4.5 L8 3.5 Q6 3 4 3.5 L4 4.5 L2.5 5.5 Z M3 7 H9 V10 H3 Z" fill="var(--brand-blue)"/></svg>
        +41 56 000 12 34
      </li>
      <li>
        <svg viewBox="0 0 12 12" aria-hidden="true"><rect x="3.5" y="1" width="5" height="10" rx="0.8" fill="none" stroke="var(--brand-blue)" stroke-width="1.2"/></svg>
        +41 79 000 56 78
      </li>
      <li>
        <svg viewBox="0 0 12 12" aria-hidden="true"><rect x="1" y="3" width="10" height="6.5" fill="none" stroke="var(--brand-blue)" stroke-width="1.1"/><path d="M1 3 L6 7 L11 3" fill="none" stroke="var(--brand-blue)" stroke-width="1.1"/></svg>
        lukas.brenner@plovrix.ch
      </li>
      <li>
        <svg viewBox="0 0 12 12" aria-hidden="true"><circle cx="6" cy="6" r="4.8" fill="none" stroke="var(--brand-blue)" stroke-width="1.1"/><ellipse cx="6" cy="6" rx="2" ry="4.8" fill="none" stroke="var(--brand-blue)" stroke-width="0.9"/><path d="M1.2 6 H10.8" stroke="var(--brand-blue)" stroke-width="0.9"/></svg>
        www.plovrix.ch
      </li>
    </ul>

    <div class="band"></div>
  </section>
</body>
</html>
```